Private Investigator needs business card with an intelligent logo

Private Investigator needs uncluttered, intelligently designed business card with simple logo. Prefer one or two colour print only. Must convey serious approach with only basic information: Business Name, "Clearmarsh Investigations"
Phone: 03 5550 1946 Email: info@clearmarsh.com.au Web: www.clearmarsh.com.au
Agents Name: Derek Hollins Title: Investigator Mobile: 0491 570 156

Thank you all very much for your designs.  There was some really excellent ideas and the choice was very hard.  I sought opinions from a number of people about which was the best one and there were a number of different choices but eventually the majority went with one design from Kavlorix.  Thank you especially to those designers that made some changes when I suggested them.

Thanks again for all your efforts and good luck with your design careers.  I will certainly use Graftnest again with the great quality of designers that made submissions.

Regards  Derek Hollins

```html
<!DOCTYPE html>
<html lang="en">
<head>
<meta charset="utf-8">
<title>Clearmarsh Investigations – Business Cards</title>
<link href="https://fonts.googleapis.com/css2?family=Source+Sans+3:wght@400;600&display=swap" rel="stylesheet">
<style>
  :root {
    --backdrop: #e6e4e0;
    --card: #050505;
    --ink: #8c8c8c;
    --ink-dim: #5e5e5e;
    --bar: #939393;
    --ring: #2a2d31;
  }
  * { box-sizing: border-box; margin: 0; padding: 0; }
  html, body {
    width: 1200px; height: 1000px; overflow: hidden;
    background: var(--backdrop);
    font-family: "Source Sans 3", "Myriad Pro", sans-serif;
    color: var(--ink);
  }
  .canvas { position: relative; width: 1200px; height: 1000px; }
  .card {
    position: absolute; width: 480px; height: 800px;
    background: var(--card);
    box-shadow: 0 10px 30px rgba(0,0,0,.25);
  }
  .card--front { left: 90px; top: 110px; }
  .card--back  { left: 630px; top: 90px; }

  .card__heading {
    position: absolute; top: 48px; left: 0; right: 0;
    text-align: center; font-size: 30px; font-weight: 400;
    letter-spacing: .3px; text-transform: uppercase;
  }
  .brand {
    position: absolute; left: 0; right: 0;
    display: flex; align-items: center; justify-content: center; gap: 18px;
  }
  .card--front .brand { top: 200px; }
  .card--back .brand { top: 120px; }
  .brand__circle {
    width: 110px; height: 110px; border-radius: 50%;
    border: 6px solid var(--ring); flex: none;
  }
  .brand__name {
    font-size: 30px; font-weight: 600; line-height: 1.1;
    text-transform: uppercase; color: var(--ink-dim);
  }

  .agent { position: absolute; left: 0; right: 0; text-align: center; }
  .card--front .agent { top: 500px; }
  .card--back .agent { top: 420px; }
  .agent__name { font-size: 32px; text-transform: uppercase; line-height: 1.1; }
  .agent__title { font-size: 31px; line-height: 1.15; }

  .contact { position: absolute; left: 0; right: 0; list-style: none; }
  .card--front .contact { top: 620px; }
  .card--back .contact { top: 535px; }
  .contact__item {
    position: relative; height: 46px;
    font-size: 28px; text-align: center; line-height: 46px;
  }
  .contact__icon {
    position: absolute; left: 36px; top: 13px; width: 20px; height: 20px;
  }
  .edge-bar { position: absolute; width: 6px; background: var(--bar); }
  .card--front .edge-bar--left { left: 0; top: 600px; height: 200px; }
  .card--back .edge-bar--left { left: 0; top: 520px; height: 160px; }
  .card--back .edge-bar--right { right: 0; top: 480px; height: 220px; }
</style>
</head>
<body>
<div class="canvas">

  <section class="card card--front">
    <h1 class="card__heading">Clearmarsh Investigations</h1>
    <div class="brand">
      <span class="brand__circle"></span>
      <span class="brand__name">Clearmarsh<br>Investigations</span>
    </div>
    <div class="agent">
      <p class="agent__name">Derek Hollins</p>
      <p class="agent__title">Investigator</p>
    </div>
    <span class="edge-bar edge-bar--left"></span>
    <ul class="contact">
      <li class="contact__item">
        <svg class="contact__icon" viewBox="0 0 20 20"><rect x="6" y="1" width="9" height="18" rx="1.5" fill="none" stroke="currentColor" stroke-width="1.4"/><line x1="9" y1="16" x2="12" y2="16" stroke="currentColor" stroke-width="1.4"/></svg>
        03 5550 1946
      </li>
      <li class="contact__item">
        <svg class="contact__icon" viewBox="0 0 20 20"><rect x="1" y="4" width="18" height="12" fill="none" stroke="currentColor" stroke-width="1.4"/><polyline points="1,4 10,11 19,4" fill="none" stroke="currentColor" stroke-width="1.4"/></svg>
        info@clearmarsh.com.au
      </li>
      <li class="contact__item">
        <svg class="contact__icon" viewBox="0 0 20 20"><circle cx="10" cy="10" r="8.5" fill="none" stroke="currentColor" stroke-width="1.4"/><ellipse cx="10" cy="10" rx="3.8" ry="8.5" fill="none" stroke="currentColor" stroke-width="1.2"/><line x1="1.5" y1="10" x2="18.5" y2="10" stroke="currentColor" stroke-width="1.2"/><line x1="3" y1="5.5" x2="17" y2="5.5" stroke="currentColor" stroke-width="1"/><line x1="3" y1="14.5" x2="17" y2="14.5" stroke="currentColor" stroke-width="1"/></svg>
        www.clearmarsh.com.au
      </li>
    </ul>
  </section>

  <section class="card card--back">
    <div class="brand">
      <span class="brand__circle"></span>
      <span class="brand__name">Clearmarsh<br>Investigations</span>
    </div>
    <div class="agent">
      <p class="agent__name">Derek Hollins</p>
      <p class="agent__title">Investigator</p>
    </div>
    <span class="edge-bar edge-bar--left"></span>
    <span class="edge-bar edge-bar--right"></span>
    <ul class="contact">
      <li class="contact__item">
        <svg class="contact__icon" viewBox="0 0 20 20"><rect x="6" y="1" width="9" height="18" rx="1.5" fill="none" stroke="currentColor" stroke-width="1.4"/><line x1="9" y1="16" x2="12" y2="16" stroke="currentColor" stroke-width="1.4"/></svg>
        03 5550 1946
      </li>
      <li class="contact__item">
        <svg class="contact__icon" viewBox="0 0 20 20"><rect x="1" y="4" width="18" height="12" fill="none" stroke="currentColor" stroke-width="1.4"/><polyline points="1,4 10,11 19,4" fill="none" stroke="currentColor" stroke-width="1.4"/></svg>
        info@clearmarsh.com.au
      </li>
      <li class="contact__item">
        <svg class="contact__icon" viewBox="0 0 20 20"><circle cx="10" cy="10" r="8.5" fill="none" stroke="currentColor" stroke-width="1.4"/><ellipse cx="10" cy="10" rx="3.8" ry="8.5" fill="none" stroke="currentColor" stroke-width="1.2"/><line x1="1.5" y1="10" x2="18.5" y2="10" stroke="currentColor" stroke-width="1.2"/><line x1="3" y1="5.5" x2="17" y2="5.5" stroke="currentColor" stroke-width="1"/><line x1="3" y1="14.5" x2="17" y2="14.5" stroke="currentColor" stroke-width="1"/></svg>
        www.clearmarsh.com.au
      </li>
    </ul>
  </section>

</div>
</body>
</html>
```